Political sign design, fonts colors and layout

I am running for Town Council.

My message is done, and *a draft is attached* with the text we wish to use. It says "Elect Dana Velloway" etc. In Maroon and White. I am not a designer, but this is somewhat close to what we are looking for.

I need help with colors and fonts, layout, spacing, and general cleanup.

I'm attaching the town high school logo:

- "B" for Brockmere: with black and white outlines on the fonts
- we want to incorporate the black and white on the fonts
- for the entire text, parts of the text, or best would be a mix

This is for signs printed and placed all over my town.

We need two versions

1. square, 4' by 4' version
2. 36" by 24" version

The smaller version will drop the three bullet pointed text, but otherwise can be identical.

The sign can only use 3 printed colors (due to printing costs.)

1. maroon,
2. white,
3. black.

The maroon should match the maroon from the high school logo attached, which I believe I did in the draft.

We also like the white border around the outside, like in the "scoreboard" design attached.

Thanks for your attention, wish me luck.

Dana

Target Market(s)

SIgns, Political market

Industry/Entity Type

Political

Font styles to use
Sans Serif
Other font styles liked:
• Arial Black, Sans Serif Bold

Requirements
Must have
• maroon background, white font.
• - black borders around fonts where appropriate
• - great spacing
• - great typeface usage
• - clean and crisp political sign, visible while driving.
• - my name "Dana Velloway" much larger like the draft, or the appropriate additional size
• - two versions, one square, and one 36" / 24"
Nice to have
• - nice borders
• - dress it up a bit, using italics and bold fonts, without making it flashy or busy.
Should not have
• Must be easily readable from a car, except for "Paid for by Friends of Dana Velloway" which can be tiny.
• Colors are noted in the description, the "Brockmere Maroon" as the background, white font, and some use of black.

```html
<!DOCTYPE html>
<html lang="en">
<head>
<meta charset="utf-8">
<title>Elect Dana Velloway – Brockmere Council Sign</title>
<link rel="stylesheet" href="https://fonts.googleapis.com/css2?family=Montserrat:ital,wght@0,400;0,500;0,600;0,800;1,800;1,900&display=swap">
<style>
  :root {
    --maroon: #6a0a2c;
    --white: #ffffff;
    --black: #000000;
    --type: "Montserrat", Arial, sans-serif;
  }
  html, body {
    margin: 0;
    padding: 0;
    width: 1200px;
    height: 800px;
    overflow: hidden;
    background: var(--white);
  }
  .sign {
    position: relative;
    width: 1200px;
    height: 800px;
    background: var(--white);
    font-family: var(--type);
    color: var(--white);
  }
  .sign__frame {
    position: absolute;
    left: 14px; top: 14px; right: 14px; bottom: 14px;
    background: var(--black);
  }
  .sign__inner-rule {
    position: absolute;
    left: 26px; top: 26px; right: 26px; bottom: 26px;
    background: var(--white);
  }
  .sign__field {
    position: absolute;
    left: 33px; top: 33px; right: 33px; bottom: 33px;
    background: var(--maroon);
  }
  .sign h1, .sign p { margin: 0; }
  .line {
    position: absolute;
    left: 0; right: 0;
    text-align: center;
    white-space: nowrap;
    line-height: 1;
  }
  .outlined {
    -webkit-text-stroke: 12px var(--black);
    paint-order: stroke fill;
  }
  .headline {
    top: 82px;
    font-size: 96px;
    letter-spacing: -1px;
  }
  .headline__lead { font-weight: 400; }
  .headline__name { font-weight: 800; }
  .office {
    top: 206px;
    font-size: 48px;
    font-weight: 400;
  }
  .slogan {
    top: 304px;
    font-size: 72px;
    font-weight: 900;
    font-style: italic;
    font-variant: small-caps;
    letter-spacing: 1px;
  }
  .tagline {
    top: 406px;
    font-size: 60px;
    font-weight: 400;
  }
  .vote-line {
    top: 530px;
    font-size: 56px;
    font-weight: 400;
  }
  .vote-line__call {
    font-size: 100px;
    font-weight: 900;
    font-style: italic;
    margin-right: 14px;
  }
  .footer-web {
    position: absolute;
    left: 130px;
    top: 700px;
    font-size: 33px;
    font-weight: 600;
    line-height: 1;
  }
  .footer-disclaimer {
    position: absolute;
    right: 62px;
    top: 708px;
    font-size: 23px;
    font-weight: 500;
    line-height: 1;
  }
</style>
</head>
<body>
  <main class="sign">
    <div class="sign__frame"></div>
    <div class="sign__inner-rule"></div>
    <div class="sign__field"></div>

    <h1 class="line headline">
      <span class="headline__lead">Elect </span><span class="headline__name outlined">Dana Velloway</span>
    </h1>
    <p class="line office">for Brockmere Councilman/Trustee</p>
    <p class="line slogan">Take Back Our Town!</p>
    <p class="line tagline">Fighting for Brockmere</p>
    <p class="line vote-line">
      <span class="vote-line__call outlined">Vote</span>Nov. 8th “Row A”
    </p>

    <p class="footer-web">www.votedana.com</p>
    <p class="footer-disclaimer">Paid for by friends of Dana Velloway</p>
  </main>
</body>
</html>
```